Vexaroo needs app design - Social app for a party on a budget

We need a design for our app called "Vexaroo", Vexaroo is an essential application that showcases the finest clubs in the city. The primary objective of the app is to provide users with insights into club ratings and beer prices, enabling them to locate the most cost-effective beer near their current location. You as a user will also have ability to rate different Additionally, users can view posts and images from various patrons, offering glimpses into the ambiance of the establishments to determine if they meet their preferences and requirements.

We imagine Vexaroo having a "gamification app desigin" as partying is like a game, you experience new adventures and take on new quests.
Allthough we are open for different designs, surprise us.

Keyfeatures:
1 - Splash/Login Page:
Allow users to log in or sign up using Orbit, Pixa, or Folk credentials.
2 - Home Page/Announcements:
Display user-generated posts from different clubs and pubs, showcasing crowd levels and overall enjoyment.
Enable users to like posts, with sorting based on likes and proximity.
Access announcements from establishments about upcoming events, entrance fees, and performances.
3 - Search Page:
Provide a map displaying nearby pubs and clubs, with basic information such as rating, beer prices, and operating hours.
4 - List Page:
Present a comprehensive list of nearby clubs and pubs, sorted initially by rating.
Allow users to sort by beer prices, location, and other criteria.
Enable users to rate establishments using a 1-5 star system, with monthly winners prominently featured on the announcement page.
5 - My page:
Allow users to revisit and upload memories, including pictures, locations, dates, and times.
Provide an option to repost pictures on Pixa.
Feature a "Refer a Friend" button for users to earn complimentary memberships by referring friends who complete the registration process.

As mentioned these are only key features we imagine this app should have, feel free to play around with the design.

Requirements
Must have
• Key features meantioned in project description

```html
<!DOCTYPE html>
<html lang="en">
<head>
<meta charset="utf-8">
<title>Vexaroo – app screens</title>
<link rel="stylesheet" href="https://fonts.googleapis.com/css2?family=EB+Garamond:wght@400;500;600;700&family=Inter:wght@500;600&display=swap">
<style>
:root{
  --stage:#000000;
  --paper:#f7f7f7;
  --white:#ffffff;
  --ink:#111111;
  --muted:#6f6f6f;
  --line:#b9b9b9;
  --star:#ffd400;
  --night-top:#1c2a4a;
  --night-mid:#231a2c;
  --night-pink:#6a1e45;
  --map-base:#eef0ea;
  --map-water:#bfe2f5;
  --photo-warm:#8a3a3a;
  --photo-neon:#3a1020;
  --photo-green:#0f3526;
  --photo-bar:#5a3a38;
  --button-grey:#6b6b6b;
}
*{box-sizing:border-box;margin:0;padding:0}
html,body{width:813px;height:1200px;overflow:hidden;background:var(--stage)}
.stage{position:absolute;left:0;top:0;width:1574px;height:2324px;transform:scale(.51652);transform-origin:0 0;background:var(--stage);font-family:"EB Garamond",Georgia,serif;color:var(--ink)}
.phone{position:absolute;width:340px;height:736px;border-radius:22px;overflow:hidden;background:var(--paper)}
.abs{position:absolute}
.status{position:absolute;left:0;top:0;width:100%;height:52px;background:var(--white);font-family:Inter,Arial,sans-serif;font-weight:600;font-size:15px}
.status .time{position:absolute;left:46px;top:19px}
.status svg{position:absolute;right:28px;top:22px}
.night{position:absolute;left:0;top:52px;width:100%;height:684px;
  background:radial-gradient(circle at 45% 18%,#5b6d8e 0,#2b3b5e 18%,transparent 40%),
  radial-gradient(circle at 30% 70%,var(--night-pink) 0,transparent 35%),
  radial-gradient(circle at 80% 85%,var(--night-pink) 0,transparent 30%),
  linear-gradient(var(--night-top),var(--night-mid) 55%,#1a1020)}
.brand{position:absolute;width:100%;text-align:center;color:var(--white);font-weight:700;letter-spacing:1px}
.center{position:absolute;width:100%;text-align:center}
.btn-light{position:absolute;left:110px;width:120px;height:41px;background:var(--white);color:var(--ink);font-size:16px;text-align:center;line-height:41px}
.social{position:absolute;top:546px;width:22px;height:22px;border-radius:50%;background:var(--white)}
.social-name{position:absolute;top:572px;width:40px;text-align:center;color:var(--white);font-size:9px}
.label{position:absolute;left:18px;font-size:16px}
.field{position:absolute;left:17px;width:306px;height:36px;border:1px solid var(--ink);border-radius:3px;background:var(--white)}
.submit{position:absolute;left:19px;width:304px;height:42px;background:var(--ink);color:var(--white);border-radius:2px;text-align:center;line-height:42px;font-size:16px;font-weight:600}
.tabs-top{position:absolute;top:64px;width:100%;font-size:16px}
.tabs-top span{position:absolute}
.tab-on{font-weight:600;color:var(--ink)}
.tab-off{color:var(--muted)}
.title{position:absolute;left:18px;font-size:20px;font-weight:600}
.date{position:absolute;left:18px;font-size:12px;color:var(--muted)}
.body{position:absolute;left:18px;width:300px;font-size:15.5px;line-height:20px}
.divider{position:absolute;left:145px;width:52px;border-top:1px solid var(--ink)}
.stars{position:absolute;right:16px;display:flex;gap:3px}
.stars svg{width:14px;height:14px}
.photo{position:absolute;left:18px;width:224px;height:149px}
.photo-peek{position:absolute;left:261px;width:90px;height:149px}
.warm{background:linear-gradient(160deg,#c04a8a,#a06030 40%,#3a2420)}
.green{background:linear-gradient(160deg,#0a1a14,var(--photo-green) 50%,#0a1a14)}
.neon{background:linear-gradient(#2a0a14,#6a1a28 30%,#2a1418)}
.barinside{background:linear-gradient(120deg,#3a2a30,var(--photo-bar) 60%,#8a5a48)}
.price{position:absolute;font-size:16px}
.left{left:18px}
.right{right:18px}
.search{position:absolute;left:16px;top:62px;font-size:13px;color:var(--muted);display:flex;align-items:center;gap:6px}
.map{position:absolute;left:0;top:224px;width:340px;height:448px;background:linear-gradient(200deg,var(--map-base) 0,var(--map-base) 55%,var(--map-water) 75%)}
.loc{position:absolute;left:18px;font-size:10px;color:var(--muted);display:flex;align-items:center;gap:5px}
.hint{position:absolute;left:18px;font-size:9.5px;color:var(--muted)}
.tabbar{position:absolute;left:0;top:672px;width:100%;height:64px;background:var(--white)}
.tabbar svg{position:absolute;top:14px;width:22px;height:22px}
.tab-mark{position:absolute;top:0;width:28px;height:4px;background:var(--ink)}
.home-ind{position:absolute;left:110px;top:723px;width:120px;height:4px;border-radius:2px;background:var(--ink)}
.home-ind.light{background:var(--white)}
.rate-stars{position:absolute;left:84px;top:176px;display:flex;gap:6px}
.rate-stars svg{width:30px;height:30px}
.comment-btn{position:absolute;left:18px;top:536px;width:305px;height:25px;background:var(--button-grey);border-radius:3px;color:var(--white);font-size:10px;text-align:center;line-height:25px}
.review{position:absolute;left:17px;width:306px;height:46px;border:1px solid var(--ink);border-radius:4px;background:var(--white)}
.review .avatar{position:absolute;left:8px;top:8px;width:28px;height:28px;border-radius:50%;background:#c9c2bd}
.review .who{position:absolute;left:42px;top:10px;font-size:10px}
.review .mini{position:absolute;left:42px;top:24px;display:flex;gap:1px}
.review .mini svg{width:6px;height:6px}
.review .quote{position:absolute;left:100px;top:8px;width:200px;font-size:9px;line-height:12px}
.share{position:absolute;right:20px;display:flex;gap:10px}
.share i{display:block;width:12px;height:12px;border:1.3px solid var(--ink);border-radius:50%}
.icon-line{fill:none;stroke:var(--ink);stroke-width:1.5;stroke-linecap:round;stroke-linejoin:round}
.icon-off{fill:none;stroke:#9a9a9a;stroke-width:1.5;stroke-linecap:round;stroke-linejoin:round}
</style>
</head>
<body>
<svg width="0" height="0" style="position:absolute">
  <defs>
    <symbol id="star-on" viewBox="0 0 24 24"><path d="M12 2l3 6.5 7 .8-5.2 4.8 1.4 7L12 17.6 5.8 21l1.4-7L2 9.3l7-.8z" fill="#ffd400" stroke="#111" stroke-width="1.4" stroke-linejoin="round"/></symbol>
    <symbol id="star-off" viewBox="0 0 24 24"><path d="M12 2l3 6.5 7 .8-5.2 4.8 1.4 7L12 17.6 5.8 21l1.4-7L2 9.3l7-.8z" fill="none" stroke="#111" stroke-width="1.4" stroke-linejoin="round"/></symbol>
    <symbol id="i-home" viewBox="0 0 24 24"><path d="M4 10l8-6 8 6v10H4z M10 20v-6h4v6"/></symbol>
    <symbol id="i-pin" viewBox="0 0 24 24"><path d="M12 21s-7-6.5-7-12a7 7 0 0114 0c0 5.5-7 12-7 12z"/><circle cx="12" cy="9" r="2.5"/></symbol>
    <symbol id="i-list" viewBox="0 0 24 24"><path d="M8 6h13M8 12h13M8 18h13M3 6h1M3 12h1M3 18h1"/></symbol>
    <symbol id="i-user" viewBox="0 0 24 24"><circle cx="12" cy="8" r="4"/><path d="M4 21c0-4 4-6 8-6s8 2 8 6"/></symbol>
    <symbol id="i-search" viewBox="0 0 24 24"><circle cx="10.5" cy="10.5" r="7"/><path d="M16 16l5 5"/></symbol>
    <symbol id="i-cam" viewBox="0 0 24 24"><path d="M3 8h4l2-3h6l2 3h4v12H3z"/><circle cx="12" cy="13" r="4"/></symbol>
    <symbol id="i-cal" viewBox="0 0 24 24"><rect x="3" y="5" width="18" height="16"/><path d="M3 10h18M8 3v4M16 3v4"/></symbol>
    <symbol id="i-clock" viewBox="0 0 24 24"><circle cx="12" cy="12" r="9"/><path d="M12 7v5l3 2"/></symbol>
    <symbol id="i-sort" viewBox="0 0 24 24"><path d="M8 4v16M8 4l-3 3M16 20V4M16 20l3-3"/></symbol>
    <symbol id="i-status" viewBox="0 0 68 12"><rect x="0" y="8" width="3" height="4" fill="#111"/><rect x="5" y="6" width="3" height="6" fill="#111"/><rect x="10" y="3" width="3" height="9" fill="#111"/><rect x="15" y="0" width="3" height="12" fill="#111"/><path d="M26 5a10 10 0 0114 0M29 8a6 6 0 018 0" fill="none" stroke="#111" stroke-width="1.8"/><circle cx="33" cy="11" r="1.3" fill="#111"/><rect x="46" y="1" width="20" height="10" rx="3" fill="#111"/></symbol>
    <symbol id="i-male" viewBox="0 0 24 56"><circle cx="12" cy="6" r="6" fill="#111"/><path d="M3 14h18v22h-4v20h-10v-20H3z" fill="#111"/></symbol>
    <symbol id="i-female" viewBox="0 0 30 56"><circle cx="15" cy="7" r="6" fill="none" stroke="#111" stroke-width="1.6"/><path d="M8 16h14l6 24h-7v14h-12v-14H2z" fill="none" stroke="#111" stroke-width="1.6" stroke-linejoin="round"/></symbol>
  </defs>
</svg>

<main class="stage">

  <!-- Splash -->
  <section class="phone" style="left:252px;top:33px">
    <div class="status"><span class="time">9:41</span><svg width="68" height="12"><use href="#i-status"/></svg></div>
    <div class="night" role="img" aria-label="Blurred crowd in a nightclub under stage lights"></div>
    <div class="brand" style="top:348px;font-size:42px">Vexaroo</div>
  </section>

  <!-- Welcome -->
  <section class="phone" style="left:616px;top:33px">
    <div class="status"><span class="time">9:41</span><svg width="68" height="12"><use href="#i-status"/></svg></div>
    <div class="night" role="img" aria-label="Blurred crowd in a nightclub under stage lights"></div>
    <div class="center" style="top:232px;color:var(--white);font-size:20px">Welcome to</div>
    <div class="brand" style="top:270px;font-size:42px">Vexaroo</div>
    <div class="btn-light" style="top:353px">Login</div>
    <div class="btn-light" style="top:409px">Sign up</div>
    <div class="center" style="top:472px;color:var(--white);font-size:13px">or</div>
    <div class="center" style="top:508px;color:var(--white);font-size:16px">Log in using</div>
    <span class="social" style="left:119px"></span>
    <span class="social" style="left:159px"></span>
    <span class="social" style="left:198px"></span>
    <span class="social-name" style="left:110px">Orbit</span>
    <span class="social-name" style="left:150px">Pixa</span>
    <span class="social-name" style="left:189px">Folk</span>
    <div class="home-ind light"></div>
  </section>

  <!-- Sign up -->
  <section class="phone" style="left:982px;top:33px">
    <div class="status"><span class="time">9:41</span><svg width="68" height="12"><use href="#i-status"/></svg></div>
    <div class="center" style="top:64px;font-size:20px;font-weight:600">Sign up</div>
    <div class="center" style="top:109px;font-size:12px;color:var(--muted)">Create your account</div>
    <div class="label" style="top:158px">Full Name</div><div class="field" style="top:182px"></div>
    <div class="label" style="top:237px">Email</div><div class="field" style="top:260px"></div>
    <div class="label" style="top:315px">Gender</div>
    <svg class="abs" style="left:126px;top:338px" width="22" height="54"><use href="#i-male"/></svg>
    <svg class="abs" style="left:187px;top:338px" width="30" height="56"><use href="#i-female"/></svg>
    <div class="label" style="top:411px">Password</div><div class="field" style="top:435px"></div>
    <div class="label" style="top:490px">Confirm Password</div><div class="field" style="top:514px"></div>
    <div class="submit" style="top:584px">Submit</div>
    <div class="center" style="top:660px;font-size:12.5px">Already have an account? <b>Login</b></div>
    <div class="home-ind"></div>
  </section>

  <!-- Announcements -->
  <section class="phone" style="left:252px;top:793px">
    <div class="status"><span class="time">9:41</span><svg width="68" height="12"><use href="#i-status"/></svg></div>
    <div class="tabs-top"><span class="tab-on" style="left:72px">Announcements</span><span class="tab-off" style="left:216px">For you</span></div>
    <div class="title" style="top:118px">Kvelden</div>
    <div class="date" style="top:143px">June 23, 2023</div>
    <div class="body" style="top:171px">Kvelden extends complimentary admission until 22:00, with a beer price set at 60kr.</div>
    <div class="body" style="top:231px"><b>Please note:</b><br>The minimum age for entry is 20 years old. DJ Solvind will be headlining tonights entertainment...</div>
    <div class="divider" style="top:338px"></div>
    <div class="title" style="top:365px">Lanternbar</div>
    <div class="date" style="top:390px">June 23, 2023</div>
    <div class="body" style="top:418px">Kvelden extends complimentary admission until 22:00, with a beer price set at 60kr.</div>
    <div class="body" style="top:478px"><b>Please note:</b><br>The minimum age for entry is 20 years old. DJ Solvind will be headlining tonights entertainment...</div>
    <div class="divider" style="top:585px"></div>
    <div class="title" style="top:612px">Marit BAR</div>
    <div class="date" style="top:637px">June 23, 2023</div>
    <nav class="tabbar">
      <span class="tab-mark" style="left:54px"></span>
      <svg style="left:56px" class="icon-line"><use href="#i-home"/></svg>
      <svg style="left:122px" class="icon-off"><use href="#i-pin"/></svg>
      <svg style="left:192px" class="icon-off"><use href="#i-list"/></svg>
      <svg style="left:261px" class="icon-off"><use href="#i-user"/></svg>
    </nav>
    <div class="home-ind"></div>
  </section>

  <!-- For you -->
  <section class="phone" style="left:616px;top:793px">
    <div class="status"><span class="time">9:41</span><svg width="68" height="12"><use href="#i-status"/></svg></div>
    <div class="tabs-top"><span class="tab-off" style="left:75px">Announcements</span><span class="abs" style="left:186px;top:3px;width:5px;height:5px;border-radius:50%;background:var(--star)"></span><span class="tab-on" style="left:210px">For you</span></div>
    <div class="title" style="top:118px">Kvelden</div>
    <div class="stars" style="top:124px"><svg><use href="#star-on"/></svg><svg><use href="#star-on"/></svg><svg><use href="#star-on"/></svg><svg><use href="#star-on"/></svg><svg><use href="#star-off"/></svg></div>
    <div class="photo warm" style="top:157px" role="img" aria-label="Crowd inside a colourful bar"></div>
    <div class="photo-peek green" style="top:157px" role="img" aria-label="Dance floor in green light"></div>
    <div class="price left" style="top:318px">Entrance: 100 Kr</div><div class="price" style="left:236px;top:318px">Beer: 80 Kr</div>
    <div class="title" style="top:373px">Lanternbar</div>
    <div class="stars" style="top:379px"><svg><use href="#star-on"/></svg><svg><use href="#star-on"/></svg><svg><use href="#star-on"/></svg><svg><use href="#star-on"/></svg><svg><use href="#star-on"/></svg></div>
    <div class="photo neon" style="top:411px" role="img" aria-label="Bar entrance with red neon sign and crowd"></div>
    <div class="photo-peek barinside" style="top:411px" role="img" aria-label="Bartender behind the counter"></div>
    <div class="price left" style="top:573px">Entrance: 0 Kr</div><div class="price" style="left:236px;top:573px">Beer: 100 Kr</div>
    <div class="title" style="top:627px">Marit BAR</div>
    <div class="stars" style="top:633px"><svg><use href="#star-on"/></svg><svg><use href="#star-on"/></svg><svg><use href="#star-on"/></svg><svg><use href="#star-off"/></svg><svg><use href="#star-off"/></svg></div>
    <div class="photo" style="top:665px;background:#3a2a2a"></div>
    <nav class="tabbar">
      <span class="tab-mark" style="left:54px"></span>
      <svg style="left:56px" class="icon-line"><use href="#i-home"/></svg>
      <svg style="left:122px" class="icon-off"><use href="#i-pin"/></svg>
      <svg style="left:192px" class="icon-off"><use href="#i-list"/></svg>
      <svg style="left:261px" class="icon-off"><use href="#i-user"/></svg>
    </nav>
    <div class="home-ind"></div>
  </section>

  <!-- Map -->
  <section class="phone" style="left:982px;top:793px">
    <div class="status"><span class="time">9:41</span><svg width="68" height="12"><use href="#i-status"/></svg></div>
    <div class="search"><svg width="18" height="18" class="icon-line"><use href="#i-search"/></svg>Search</div>
    <div class="title" style="top:105px">Kvelden</div>
    <div class="stars" style="top:111px"><svg><use href="#star-on"/></svg><svg><use href="#star-on"/></svg><svg><use href="#star-on"/></svg><svg><use href="#star-on"/></svg><svg><use href="#star-off"/></svg></div>
    <div class="price left" style="top:136px">Entrance: 0 Kr</div><div class="price right" style="top:136px">Beer: 110 Kr</div>
    <div class="price left" style="top:160px">Age: 21 +</div>
    <div class="price left" style="top:183px">Opens: 20:00 - 03:00</div>
    <div class="map" role="img" aria-label="City street map with pins marking nearby bars and clubs"></div>
    <nav class="tabbar">
      <span class="tab-mark" style="left:120px"></span>
      <svg style="left:56px" class="icon-off"><use href="#i-home"/></svg>
      <svg style="left:122px" class="icon-line"><use href="#i-pin"/></svg>
      <svg style="left:192px" class="icon-off"><use href="#i-list"/></svg>
      <svg style="left:261px" class="icon-off"><use href="#i-user"/></svg>
    </nav>
    <div class="home-ind"></div>
  </section>

  <!-- List -->
  <section class="phone" style="left:252px;top:1554px">
    <div class="status"><span class="time">9:41</span><svg width="68" height="12"><use href="#i-status"/></svg></div>
    <div class="search"><svg width="18" height="18" class="icon-line"><use href="#i-search"/></svg>Search</div>
    <svg class="abs icon-line" style="left:305px;top:64px" width="18" height="18"><use href="#i-sort"/></svg>
    <div class="hint" style="top:106px">Please tap for more details</div>

    <div class="title" style="top:130px">Kvelden</div>
    <div class="stars" style="top:136px"><svg><use href="#star-on"/></svg><svg><use href="#star-on"/></svg><svg><use href="#star-on"/></svg><svg><use href="#star-on"/></svg><svg><use href="#star-off"/></svg></div>
    <div class="price left" style="top:161px">Entrance: 100 Kr</div><div class="price" style="left:236px;top:161px">Beer: 80 Kr</div>
    <div class="loc" style="top:185px"><svg width="12" height="12" class="icon-line"><use href="#i-pin"/></svg>Kvartal Nord, Oslo</div>

    <div class="title" style="top:230px">Lanternbar</div>
    <div class="stars" style="top:236px"><svg><use href="#star-on"/></svg><svg><use href="#star-on"/></svg><svg><use href="#star-on"/></svg><svg><use href="#star-on"/></svg><svg><use href="#star-on"/></svg></div>
    <div class="price left" style="top:261px">Entrance: 0 Kr</div><div class="price" style="left:236px;top:261px">Beer: 80 Kr</div>
    <div class="loc" style="top:285px"><svg width="12" height="12" class="icon-line"><use href="#i-pin"/></svg>Kvartal Nord, Oslo</div>

    <div class="title" style="top:330px">Marit BAR</div>
    <div class="stars" style="top:336px"><svg><use href="#star-on"/></svg><svg><use href="#star-on"/></svg><svg><use href="#star-on"/></svg><svg><use href="#star-on"/></svg><svg><use href="#star-on"/></svg></div>
    <div class="price left" style="top:361px">Entrance: 0 Kr</div><div class="price" style="left:236px;top:361px">Beer: 100 Kr</div>
    <div class="loc" style="top:385px"><svg width="12" height="12" class="icon-line"><use href="#i-pin"/></svg>Kvartal Nord, Oslo</div>

    <div class="title" style="top:430px">Blikk</div>
    <div class="stars" style="top:436px"><svg><use href="#star-on"/></svg><svg><use href="#star-on"/></svg><svg><use href="#star-on"/></svg><svg><use href="#star-off"/></svg><svg><use href="#star-off"/></svg></div>
    <div class="price left" style="top:461px">Entrance: 80 Kr</div><div class="price" style="left:236px;top:461px">Beer: 80 Kr</div>
    <div class="loc" style="top:485px"><svg width="12" height="12" class="icon-line"><use href="#i-pin"/></svg>Kvartal Nord, Oslo</div>

    <div class="title" style="top:530px">Nordlys</div>
    <div class="stars" style="top:536px"><svg><use href="#star-on"/></svg><svg><use href="#star-on"/></svg><svg><use href="#star-on"/></svg><svg><use href="#star-on"/></svg><svg><use href="#star-on"/></svg></div>
    <div class="price left" style="top:561px">Entrance: 0 Kr</div><div class="price" style="left:236px;top:561px">Beer: 100 Kr</div>
    <div class="loc" style="top:585px"><svg width="12" height="12" class="icon-line"><use href="#i-pin"/></svg>Kvartal Nord, Oslo</div>

    <div class="title" style="top:630px">Vaktbua</div>
    <div class="stars" style="top:636px"><svg><use href="#star-on"/></svg><svg><use href="#star-on"/></svg><svg><use href="#star-on"/></svg><svg><use href="#star-on"/></svg><svg><use href="#star-on"/></svg></div>
    <div class="price left" style="top:661px">Entrance: 0 Kr</div><div class="price" style="left:236px;top:661px">Beer: 80 Kr</div>
    <nav class="tabbar">
      <span class="tab-mark" style="left:189px"></span>
      <svg style="left:56px" class="icon-off"><use href="#i-home"/></svg>
      <svg style="left:122px" class="icon-off"><use href="#i-pin"/></svg>
      <svg style="left:192px" class="icon-line"><use href="#i-list"/></svg>
      <svg style="left:261px" class="icon-off"><use href="#i-user"/></svg>
    </nav>
    <div class="home-ind"></div>
  </section>

  <!-- Rating -->
  <section class="phone" style="left:616px;top:1554px">
    <div class="status"><span class="time">9:41</span><svg width="68" height="12"><use href="#i-status"/></svg></div>
    <div class="center" style="top:64px;font-size:21px;font-weight:600">How was your experience ?</div>
    <div class="hint" style="top:106px">Rate your enjoyment</div>
    <div class="title" style="top:134px">Lanternbar</div>
    <div class="rate-stars"><svg><use href="#star-on"/></svg><svg><use href="#star-off"/></svg><svg><use href="#star-off"/></svg><svg><use href="#star-off"/></svg><svg><use href="#star-off"/></svg></div>
    <div class="photo neon" style="top:224px" role="img" aria-label="Bar entrance with red neon sign and crowd"></div>
    <div class="photo-peek barinside" style="top:224px" role="img" aria-label="Bartender behind the counter"></div>
    <div class="price left" style="top:386px">Entrance: 0 Kr</div><div class="price" style="left:236px;top:386px">Beer: 100 Kr</div>
    <div class="price left" style="top:409px">Age: 21 +</div>
    <div class="price left" style="top:432px">Opens: 20:00 - 03:00</div>
    <div class="loc" style="top:460px"><svg width="12" height="12" class="icon-line"><use href="#i-pin"/></svg>Kvartal Nord, Oslo</div>
    <div class="abs" style="left:18px;top:513px;font-size:13px">Share your experience</div>
    <div class="comment-btn">Leave a Comment</div>
    <div class="review" style="top:575px">
      <span class="avatar" role="img" aria-label="Reviewer avatar"></span>
      <span class="who">Tomas</span>
      <span class="mini"><svg><use href="#star-on"/></svg><svg><use href="#star-on"/></svg><svg><use href="#star-on"/></svg><svg><use href="#star-on"/></svg><svg><use href="#star-on"/></svg></span>
      <span class="quote">“Perfect for locals and visitors alike, it’s a must-visit for an unforgettable evening!”</span>
    </div>
    <div class="review" style="top:628px">
      <span class="avatar" role="img" aria-label="Reviewer avatar"></span>
      <span class="who">Ingrid</span>
      <span class="mini"><svg><use href="#star-on"/></svg><svg><use href="#star-on"/></svg><svg><use href="#star-on"/></svg><svg><use href="#star-on"/></svg><svg><use href="#star-on"/></svg></span>
      <span class="quote">“The bar staff is welcoming and efficient, adding to the overall positive vibe of the place.”</span>
    </div>
    <nav class="tabbar">
      <span class="tab-mark" style="left:189px"></span>
      <svg style="left:56px" class="icon-off"><use href="#i-home"/></svg>
      <svg style="left:122px" class="icon-off"><use href="#i-pin"/></svg>
      <svg style="left:192px" class="icon-line"><use href="#i-list"/></svg>
      <svg style="left:261px" class="icon-off"><use href="#i-user"/></svg>
    </nav>
    <div class="home-ind"></div>
  </section>

  <!-- Profile -->
  <section class="phone" style="left:982px;top:1554px">
    <div class="status"><span class="time">9:41</span><svg width="68" height="12"><use href="#i-status"/></svg></div>
    <div class="center" style="top:64px;font-size:21px;font-weight:600">Profile</div>
    <span class="abs" style="left:296px;top:64px;width:28px;height:28px;border-radius:50%;background:#5a5a5a;border:1.5px solid var(--ink)" role="img" aria-label="User profile picture"></span>
    <div class="tabs-top" style="top:110px;font-size:13px"><span class="tab-on" style="left:38px">My Memories</span><span class="tab-off" style="left:154px">Refer a Friend</span><span class="tab-off" style="left:264px">Setting</span></div>

    <div class="title" style="top:145px">Kvelden</div>
    <svg class="abs icon-line" style="left:300px;top:146px" width="22" height="22"><use href="#i-cam"/></svg>
    <div class="photo warm" style="top:176px" role="img" aria-label="Crowd inside a colourful bar"></div>
    <div class="photo-peek green" style="top:176px" role="img" aria-label="Dance floor in green light"></div>
    <div class="loc" style="top:339px"><svg width="12" height="12" class="icon-line"><use href="#i-pin"/></svg>Kvartal Nord, Oslo</div>
    <div class="loc" style="top:359px"><svg width="12" height="12" class="icon-line"><use href="#i-cal"/></svg>March 6, 2023</div>
    <div class="loc" style="top:379px"><svg width="12" height="12" class="icon-line"><use href="#i-clock"/></svg>01:00</div>
    <div class="share" style="top:340px"><i></i><i></i><i></i></div>

    <div class="title" style="top:420px">Lanternbar</div>
    <svg class="abs icon-line" style="left:300px;top:421px" width="22" height="22"><use href="#i-cam"/></svg>
    <div class="photo neon" style="top:451px" role="img" aria-label="Bar entrance with red neon sign and crowd"></div>
    <div class="photo-peek barinside" style="top:451px" role="img" aria-label="Bartender behind the counter"></div>
    <div class="loc" style="top:614px"><svg width="12" height="12" class="icon-line"><use href="#i-pin"/></svg>Kvartal Nord, Oslo</div>
    <div class="loc" style="top:634px"><svg width="12" height="12" class="icon-line"><use href="#i-cal"/></svg>March 6, 2023</div>
    <div class="loc" style="top:654px"><svg width="12" height="12" class="icon-line"><use href="#i-clock"/></svg>01:00</div>
    <div class="share" style="top:615px"><i></i><i></i><i></i></div>
    <nav class="tabbar">
      <span class="tab-mark" style="left:258px"></span>
      <svg style="left:56px" class="icon-off"><use href="#i-home"/></svg>
      <svg style="left:122px" class="icon-off"><use href="#i-pin"/></svg>
      <svg style="left:192px" class="icon-off"><use href="#i-list"/></svg>
      <svg style="left:261px" class="icon-line"><use href="#i-user"/></svg>
    </nav>
    <div class="home-ind"></div>
  </section>

</main>
</body>
</html>
```